Marketing Webpage to Sell to Doctors

We need a page design made to improve a marketing site that signs doctors up for a marketing program. Based on the existing site design, we need a new version created to improve the credibility of the solution and include screenshots of the product.

Target Market(s)

Doctors

Industry/Entity Type

Health And Wellness

Number of Pages Required

1 page

Requirements
Must have
• This is the page to redesign: https://www.brevantis.com/doctor-marketing/add-listing
• Use screenshots attached as well as two profile picture from one of these profiles. Use one with before and after photos.
• http://www.brevantis.com/tomas-r-velkin-md-dmd
• http://www.brevantis.com/oskar-d-fennimore-md
Nice to have
• The style can stay as it is, and add in 5 screenshots. one with b&a pictures, general profile, dashboard, lead view to showcase the actual product the doctor is buying.

```html
<!DOCTYPE html>
<html lang="en">
<head>
<meta charset="utf-8">
<title>Brevantis – Doctor Listing</title>
<link href="https://fonts.googleapis.com/css2?family=Open+Sans:wght@400;600;700;800&display=swap" rel="stylesheet">
<style>
:root{
  --red:#c3283b;
  --red-dark:#9e1d2e;
  --teal:#2f6a6b;
  --teal-dark:#1f4f50;
  --ink:#333;
  --muted:#777;
  --line:#dcdcdc;
  --sand:#ece5d8;
  --sand-dark:#d9cfbd;
  --white:#fff;
}
*{box-sizing:border-box;margin:0;padding:0}
html,body{width:709px;height:1200px;overflow:hidden}
body{font-family:"Open Sans",Arial,sans-serif;color:var(--ink);background:var(--white);font-size:9px;line-height:1.35}
.wrap{width:626px;margin:0 auto;position:relative}

/* top bar */
.topbar{height:70px}
.topbar .wrap{display:flex;justify-content:space-between;align-items:center;height:70px}
.brand{display:flex;align-items:center;gap:6px}
.brand-mark{width:14px;height:14px;background:var(--red);border-radius:50%}
.brand-name{font-size:22px;font-weight:700;color:var(--red);letter-spacing:-.3px}
.brand-tag{font-size:6.5px;color:var(--muted);margin-top:-2px}
.util-nav{display:flex;gap:14px;font-size:7px;font-weight:600;color:#555;text-transform:uppercase}

/* main nav */
.mainnav{background:var(--red);height:30px;border-bottom:2px solid var(--red-dark)}
.mainnav ul{list-style:none;display:flex;justify-content:space-between;height:28px;align-items:center;width:626px;margin:0 auto;padding:0 10px}
.mainnav li{color:var(--white);font-size:7.5px;font-weight:700;text-transform:uppercase}

/* hero */
.hero{height:386px;background:linear-gradient(135deg,var(--teal) 0%,var(--teal-dark) 100%);position:relative;overflow:hidden}
.hero .wrap{height:386px}
.signup{position:absolute;left:0;top:18px;width:196px;background:var(--white);box-shadow:0 2px 8px rgba(0,0,0,.3)}
.signup-head{background:var(--red);color:var(--white);padding:10px 12px 9px;font-weight:800;line-height:1.1}
.signup-head .big{font-size:14px;display:block}
.signup-head .small{font-size:8px}
.signup form{padding:10px 12px 12px}
.field{display:block;width:100%;height:22px;border:1px solid var(--line);margin-bottom:6px;font-size:7.5px;color:#999;padding:5px 6px;background:#fafafa}
.submit{display:inline-block;background:var(--red);color:var(--white);font-size:7.5px;font-weight:700;padding:6px 10px;margin-top:4px;text-transform:uppercase}

.pitch{position:absolute;left:220px;top:30px;width:210px;color:var(--white)}
.pitch h1{font-size:17px;font-weight:800;line-height:1.1}
.pitch h2{font-size:12px;font-weight:600;margin-top:4px}
.pitch p{font-size:7.5px;margin-top:8px;opacity:.9}
.pitch h3{font-size:11px;font-weight:700;margin-top:12px}
.checks{list-style:none;margin-top:8px}
.checks li{display:flex;align-items:center;gap:6px;font-size:7.8px;margin-bottom:6px}
.checks svg{flex:none}
.hero-photo{position:absolute;right:0;top:18px;width:200px;height:368px;background:linear-gradient(180deg,#e8eef0 0%,#c9d6da 100%)}

/* doctor rows */
.doctors{padding-top:14px}
.doc-row{display:flex;justify-content:space-between;height:100px}
.doc-info{width:360px}
.doc-name{color:var(--red);font-size:12px;font-weight:700}
.doc-spec{font-size:7.5px;color:var(--muted);margin-bottom:6px}
.doc-body{display:flex;gap:10px}
.doc-video{width:110px;height:62px;background:linear-gradient(135deg,#5a6b78,#2d3944);flex:none}
.doc-practice{font-size:10px;font-weight:700;line-height:1.15}
.doc-text{font-size:6.5px;color:#666;margin-top:3px}
.ba{width:232px}
.ba h4{font-size:11px;font-weight:700}
.ba a{font-size:7px;color:var(--red);text-decoration:none}
.ba-pair{display:flex;gap:3px;margin-top:4px}
.ba-shot{width:115px;height:58px;background:linear-gradient(180deg,#e2b9a1,#c79278);position:relative}
.ba-shot span{position:absolute;right:4px;top:3px;font-size:6.5px;color:var(--white)}

/* solutions */
.solutions{border-top:1px solid var(--line);margin-top:12px;padding-top:14px;display:flex;gap:26px}
.dash{width:290px;height:200px;border:1px solid var(--line);padding:6px;background:var(--white);box-shadow:0 1px 4px rgba(0,0,0,.15)}
.dash-fill{width:100%;height:100%;background:linear-gradient(180deg,#f1f4f6,#dde4e9)}
.sol h2{font-size:17px;font-weight:700;line-height:1.1}
.sol h3{font-size:10px;font-weight:600;color:#555}
.partner{display:flex;align-items:center;gap:5px;margin:6px 0 8px}
.partner i{width:10px;height:10px;background:var(--teal);display:block}
.partner b{font-size:11px;color:var(--teal);font-weight:700}
.sol ul{list-style:none}
.sol li{font-size:7.8px;padding:2px 0 2px 10px;position:relative}
.sol li::before{content:"";position:absolute;left:0;top:6px;width:4px;height:4px;background:var(--red);border-radius:50%}

/* footer */
.footer{position:absolute;left:0;top:960px;width:709px;height:210px;background:var(--sand);border-top:6px solid var(--sand-dark)}
.footer .wrap{display:flex;gap:24px;padding-top:12px}
.footer h5{font-size:9px;font-weight:700;text-transform:uppercase;margin-bottom:8px;color:#444}
.testimonial{width:330px}
.testi-body{display:flex;gap:10px}
.avatar{width:52px;height:52px;border-radius:50%;background:linear-gradient(135deg,#b9a79a,#7c6a5e);flex:none}
.testi-body p{font-size:7px;color:#555}
.testi-by{font-size:7px;font-weight:700;margin-top:5px}
.links{width:120px;list-style:none}
.links li{font-size:7px;color:#555;margin-bottom:3px}
.contact p{font-size:7px;color:#555;margin-bottom:3px}
.social{display:flex;gap:4px;margin-top:6px}
.social span{width:12px;height:12px;border-radius:50%;background:var(--red);display:block}
.copy{position:absolute;left:0;top:1170px;width:709px;height:30px;background:var(--red);color:var(--white);font-size:7px;text-align:center;line-height:30px}
</style>
</head>
<body>

<header class="topbar">
  <div class="wrap">
    <div>
      <div class="brand"><span class="brand-mark"></span><span class="brand-name">Brevantis.com</span></div>
      <div class="brand-tag">Find the right doctor for you</div>
    </div>
    <nav class="util-nav"><span>Home</span><span>Blog</span><span>Newsletter Signup</span><span>Doctor Reviews</span><span>Sign In</span></nav>
  </div>
</header>

<nav class="mainnav">
  <ul>
    <li>Find a Doctor</li><li>Learn More</li><li>Before and After Gallery</li><li>Resources</li><li>Financing</li><li>Doctors Only</li>
  </ul>
</nav>

<section class="hero">
  <div class="wrap">
    <div class="signup">
      <div class="signup-head"><span class="small">OR START YOUR</span><span class="big">FREE DOCTOR</span><span class="small">LISTING NOW</span></div>
      <form>
        <span class="field">Name</span>
        <span class="field">Email</span>
        <span class="field">Specialty</span>
        <span class="field">Phone Number</span>
        <span class="field">Practice</span>
        <span class="field">Zip</span>
        <span class="submit">Submit Request</span>
      </form>
    </div>

    <div class="pitch">
      <h1>WANT MORE PATIENT LEADS?</h1>
      <h2>List your medical practice on Brevantis</h2>
      <p>Since 1999, Brevantis.com has been the top patient lead generation network used by doctors marketing elective procedures and services to new patients nationwide.</p>
      <h3>Brevantis.com allows you to:</h3>
      <ul class="checks">
        <li><svg width="10" height="10" viewBox="0 0 10 10"><circle cx="5" cy="5" r="5" fill="#fff"/><path d="M2.6 5.2l1.6 1.6 3.2-3.4" stroke="#c3283b" stroke-width="1.4" fill="none"/></svg>Receive unlimited patient leads</li>
        <li><svg width="10" height="10" viewBox="0 0 10 10"><circle cx="5" cy="5" r="5" fill="#fff"/><path d="M2.6 5.2l1.6 1.6 3.2-3.4" stroke="#c3283b" stroke-width="1.4" fill="none"/></svg>Customize your profile 24/7</li>
        <li><svg width="10" height="10" viewBox="0 0 10 10"><circle cx="5" cy="5" r="5" fill="#fff"/><path d="M2.6 5.2l1.6 1.6 3.2-3.4" stroke="#c3283b" stroke-width="1.4" fill="none"/></svg>Manage all patient leads in one spot</li>
        <li><svg width="10" height="10" viewBox="0 0 10 10"><circle cx="5" cy="5" r="5" fill="#fff"/><path d="M2.6 5.2l1.6 1.6 3.2-3.4" stroke="#c3283b" stroke-width="1.4" fill="none"/></svg>Send automated email messages to all new leads</li>
        <li><svg width="10" height="10" viewBox="0 0 10 10"><circle cx="5" cy="5" r="5" fill="#fff"/><path d="M2.6 5.2l1.6 1.6 3.2-3.4" stroke="#c3283b" stroke-width="1.4" fill="none"/></svg>Track all special and regional leads</li>
        <li><svg width="10" height="10" viewBox="0 0 10 10"><circle cx="5" cy="5" r="5" fill="#fff"/><path d="M2.6 5.2l1.6 1.6 3.2-3.4" stroke="#c3283b" stroke-width="1.4" fill="none"/></svg>Share gallery updates and positive recommendations</li>
        <li><svg width="10" height="10" viewBox="0 0 10 10"><circle cx="5" cy="5" r="5" fill="#fff"/><path d="M2.6 5.2l1.6 1.6 3.2-3.4" stroke="#c3283b" stroke-width="1.4" fill="none"/></svg>Measure your return on investment (ROI)</li>
      </ul>
    </div>

    <div class="hero-photo" role="img" aria-label="Smiling doctor in a white coat with a stethoscope"></div>
  </div>
</section>

<main class="wrap doctors">
  <div class="doc-row">
    <div class="doc-info">
      <div class="doc-name">Oskar D. Fennimore, M.D.</div>
      <div class="doc-spec">Cosmetic Treatments and Eye Care Procedures</div>
      <div class="doc-body">
        <div class="doc-video" role="img" aria-label="Video still of the doctor speaking in his office"></div>
        <div>
          <div class="doc-practice">Desert Ridge Eye Institute &amp;<br>Cosmetic Laser Center</div>
          <p class="doc-text">Dr. Fennimore leads a practice focused on vision correction and aesthetic care. His team offers laser procedures, eyelid surgery and skin treatments, and patients from across the region choose the clinic for its careful, personal approach.</p>
        </div>
      </div>
    </div>
    <div class="ba">
      <h4>Before and After Photos</h4>
      <a>view all galleries</a>
      <div class="ba-pair">
        <div class="ba-shot" role="img" aria-label="Before photo of treated eye area"><span>before</span></div>
        <div class="ba-shot" role="img" aria-label="After photo of treated eye area"><span>after</span></div>
      </div>
    </div>
  </div>

  <div class="doc-row">
    <div class="doc-info">
      <div class="doc-name">Tomas R. Velkin, M.D., D.M.D.</div>
      <div class="doc-spec">Double Board Certified Plastic Surgeon</div>
      <div class="doc-body">
        <div class="doc-video" role="img" aria-label="Video still of the surgeon at his desk"></div>
        <div>
          <div class="doc-practice">Velkin Plastic Surgery<br><span style="font-size:7.5px;font-weight:400">Redefining Youth</span></div>
          <p class="doc-text">Dr. Velkin brings training in medicine and dentistry to facial and body surgery. His videos explain each procedure clearly, helping patients feel informed and confident before their first consultation.</p>
        </div>
      </div>
    </div>
    <div class="ba">
      <h4>Before and After Photos</h4>
      <a>view all galleries</a>
      <div class="ba-pair">
        <div class="ba-shot" role="img" aria-label="Before photo of facial profile"><span>before</span></div>
        <div class="ba-shot" role="img" aria-label="After photo of facial profile"><span>after</span></div>
      </div>
    </div>
  </div>

  <section class="solutions">
    <div class="dash"><div class="dash-fill" role="img" aria-label="Screenshot of the doctor dashboard showing lead statistics"></div></div>
    <div class="sol">
      <h2>Online Marketing Solutions</h2>
      <h3>for Doctors by ClinicHarbor</h3>
      <div class="partner"><i></i><b>ClinicHarbor</b></div>
      <ul>
        <li>Patient Lead Network</li>
        <li>Website Design &amp; Content Manager</li>
        <li>Mobile Website Interface Design</li>
        <li>Video Services &amp; Production</li>
        <li>Advanced SEO Medical Marketing</li>
        <li>Call Tracking, Recording &amp; Staff Training</li>
        <li>Keyword Marketing - Pay Per Click (PPC) Advertising</li>
        <li>Patient Education 3D Animations</li>
      </ul>
    </div>
  </section>
</main>

<footer class="footer">
  <div class="wrap">
    <div class="testimonial">
      <h5>What Our Patients Say</h5>
      <div class="testi-body">
        <div class="avatar" role="img" aria-label="Patient portrait"></div>
        <div>
          <p>“I found a wonderful surgeon close to home in minutes. The reviews and photos helped me decide, and booking my consultation was simple. I recommend this site to friends.”</p>
          <div class="testi-by">— Jane M., Austin</div>
        </div>
      </div>
    </div>
    <ul class="links">
      <h5>Information</h5>
      <li>Home</li><li>Find a Doctor</li><li>Before and After Gallery</li><li>Resources</li><li>Financing</li><li>Doctors Only</li>
    </ul>
    <div class="contact">
      <h5>Contact Us</h5>
      <p>Brevantis.com, Suite 200</p>
      <p>Portland, OR 97201</p>
      <p>1-800-555-0133</p>
      <p>info@brevantis.com</p>
      <div class="social"><span></span><span></span><span></span><span></span><span></span></div>
    </div>
  </div>
</footer>
<div class="copy">Copyright © 2015 Brevantis.com · All rights reserved.</div>

</body>
</html>
```